Professional Business Cards for Janitorial Company

We are a Janitorial Company that services Commercial Buildings.

Our Logo is included. It can't look silly or cartoonish. Has to look professional.

Information:
Derek Malloy
Operations Manager
619.437.2086
DMalloy@BrightwayFacilityCare.com
www.BrightwayFacilityCare.com

```html
<!DOCTYPE html>
<html lang="en">
<head>
<meta charset="utf-8">
<title>Brightway Facility Care — Business Cards</title>
<link rel="stylesheet" href="https://fonts.googleapis.com/css2?family=Open+Sans:wght@300;400;600&display=swap">
<style>
  :root {
    --canvas-bg: #e9ebee;
    --card-white: #ffffff;
    --brand-cyan: #14bdee;
    --ink-dark: #2f3338;
    --ink-soft: #4a4f55;
    --icon-tile: #eef1f4;
    --icon-edge: #c9d0d6;
    --icon-blue: #3aa6d9;
    --card-shadow: 0 14px 30px rgba(30, 40, 55, 0.18);
  }
  * { box-sizing: border-box; margin: 0; padding: 0; }
  html, body {
    width: 1200px; height: 857px; overflow: hidden;
    background: var(--canvas-bg);
    font-family: "Open Sans", Arial, sans-serif;
  }
  .canvas { position: relative; width: 1200px; height: 857px; }

  .card {
    position: absolute; width: 560px; height: 320px;
    background: var(--card-white);
    box-shadow: var(--card-shadow);
    overflow: hidden;
  }

  /* Back: logo side */
  .card-back { left: 580px; top: 100px; }
  .card-back .brand-band {
    position: absolute; left: 0; right: 0; bottom: 0; height: 150px;
    background: var(--brand-cyan);
  }
  .brand-lockup {
    position: absolute; left: 250px; top: 62px;
    display: flex; align-items: center; gap: 14px;
  }
  .brand-mark {
    width: 46px; height: 46px;
    border: 5px solid var(--brand-cyan);
  }
  .brand-name {
    color: var(--brand-cyan); font-weight: 600;
    font-size: 22px; line-height: 1.1;
  }

  /* Front: contact side */
  .card-front { left: 80px; top: 460px; }
  .card-front .front-panel {
    position: absolute; inset: 0; width: 100%; height: 100%;
  }
  .identity { position: absolute; left: 56px; top: 118px; }
  .person-name {
    font-weight: 300; font-size: 34px; color: var(--ink-dark);
    line-height: 1.1;
  }
  .person-title {
    font-size: 14px; color: var(--ink-soft); margin-top: 2px;
  }
  .contact-row {
    position: absolute; left: 14px; right: 14px; top: 200px;
    display: grid; grid-template-columns: 1.35fr 0.8fr 1.15fr;
    text-align: center;
  }
  .contact-item { display: flex; flex-direction: column; align-items: center; gap: 10px; }
  .contact-icon { width: 34px; height: 34px; }
  .contact-text { font-size: 10.5px; color: var(--ink-soft); white-space: nowrap; }
</style>
</head>
<body>
<main class="canvas">

  <section class="card card-back" aria-label="Card back">
    <div class="brand-band"></div>
    <div class="brand-lockup">
      <span class="brand-mark"></span>
      <span class="brand-name">Brightway<br>Facility Care</span>
    </div>
  </section>

  <section class="card card-front" aria-label="Card front">
    <svg class="front-panel" viewBox="0 0 560 320" preserveAspectRatio="none" aria-hidden="true">
      <polygon points="0,0 560,0 560,176 0,196" fill="var(--brand-cyan)"/>
    </svg>

    <div class="identity">
      <h1 class="person-name">Derek Malloy</h1>
      <p class="person-title">Operations Manager</p>
    </div>

    <div class="contact-row">
      <div class="contact-item">
        <svg class="contact-icon" viewBox="0 0 34 34" aria-hidden="true">
          <path d="M3 3h28v22H20l-3 5-3-5H3z" fill="var(--icon-tile)" stroke="var(--icon-edge)"/>
          <rect x="8" y="8" width="18" height="12" fill="var(--icon-blue)"/>
          <path d="M8 8l9 7 9-7" fill="none" stroke="#fff" stroke-width="1.5"/>
        </svg>
        <span class="contact-text">DMalloy@BrightwayFacilityCare.com</span>
      </div>
      <div class="contact-item">
        <svg class="contact-icon" viewBox="0 0 34 34" aria-hidden="true">
          <path d="M3 3h28v22H20l-3 5-3-5H3z" fill="var(--icon-tile)" stroke="var(--icon-edge)"/>
          <rect x="12" y="6" width="10" height="17" rx="2" fill="var(--icon-blue)"/>
          <rect x="14" y="8" width="6" height="9" fill="#fff"/>
          <circle cx="17" cy="20" r="1.2" fill="#fff"/>
        </svg>
        <span class="contact-text">619.437.2086</span>
      </div>
      <div class="contact-item">
        <svg class="contact-icon" viewBox="0 0 34 34" aria-hidden="true">
          <path d="M3 3h28v22H20l-3 5-3-5H3z" fill="var(--icon-tile)" stroke="var(--icon-edge)"/>
          <circle cx="17" cy="14" r="8" fill="var(--icon-blue)"/>
          <path d="M9 14h16M17 6c-4 4-4 12 0 16M17 6c4 4 4 12 0 16" fill="none" stroke="#fff" stroke-width="1"/>
        </svg>
        <span class="contact-text">www.BrightwayFacilityCare.com</span>
      </div>
    </div>
  </section>

</main>
</body>
</html>
```